Halvex Consulting

Hi,
I have my own network consulting business (just me)
and need to get a logo and business card design together,

Based in New Zealand,

Gareth Pollard
Unified Communications and Network Architect

/design engineer,
and would like this to be the basis for personal branding and company identity

Reason: I will be off site for a couple of days - so you have some more time

Business

• I have the basis for a optional logo - needs color -

```html
<!DOCTYPE html>
<html lang="en">
<head>
<meta charset="utf-8">
<title>Halvex Consulting – Business Card</title>
<link rel="stylesheet" href="https://fonts.googleapis.com/css2?family=Saira+Condensed:wght@600&family=Arimo:wght@700&family=Tinos:ital@1&display=swap">
<style>
  :root {
    --red: #d71313;
    --red-deep: #c40c0c;
    --white: #ffffff;
    --ink: #3a3a3a;
    --ink-soft: #4a4a4a;
    --edge: #d9d9d9;
    --page: #ffffff;
  }
  html, body {
    margin: 0;
    padding: 0;
    width: 1060px;
    height: 1200px;
    overflow: hidden;
    background: var(--page);
  }
  .card {
    position: absolute;
    left: 0;
    width: 1058px;
    border: 1px solid var(--edge);
    border-radius: 24px;
    overflow: hidden;
  }
  .card-front {
    top: 0;
    height: 584px;
    background: var(--white);
  }
  .card-back {
    top: 609px;
    height: 586px;
    background: linear-gradient(180deg, var(--red) 0%, var(--red-deep) 100%);
  }
  .front-band {
    position: absolute;
    inset: 0;
    width: 100%;
    height: 100%;
  }
  .holder-name {
    position: absolute;
    left: 578px;
    top: 34px;
    margin: 0;
    font-family: "Tinos", "Times New Roman", serif;
    font-style: italic;
    font-weight: 400;
    font-size: 44px;
    color: var(--ink);
    letter-spacing: 0.5px;
  }
  .name-rule {
    position: absolute;
    left: 560px;
    top: 95px;
    width: 460px;
    height: 2px;
    background: var(--ink-soft);
  }
  .holder-role {
    position: absolute;
    right: 34px;
    top: 112px;
    margin: 0;
    font-family: "Arimo", Arial, sans-serif;
    font-weight: 700;
    font-size: 33px;
    line-height: 43px;
    text-align: right;
    color: var(--ink-soft);
  }
  .brand-mark {
    position: absolute;
    left: 46px;
    top: 228px;
    display: flex;
    align-items: center;
    gap: 16px;
  }
  .brand-dot {
    width: 44px;
    height: 44px;
    border-radius: 50%;
    background: var(--red);
  }
  .brand-word {
    font-family: "Saira Condensed", "Arial Narrow", sans-serif;
    font-weight: 600;
    font-size: 64px;
    color: var(--ink);
    line-height: 1;
  }
  .company-name {
    position: absolute;
    left: 42px;
    top: 488px;
    margin: 0;
    font-family: "Saira Condensed", "Arial Narrow", sans-serif;
    font-weight: 600;
    font-size: 50px;
    letter-spacing: 1px;
    color: var(--white);
    line-height: 1;
  }
  .back-mark {
    position: absolute;
    left: 46px;
    top: 170px;
    font-family: "Saira Condensed", "Arial Narrow", sans-serif;
    font-weight: 600;
    font-size: 96px;
    color: rgba(255, 255, 255, 0.32);
    line-height: 1;
  }
  .contact {
    position: absolute;
    left: 370px;
    top: 232px;
    margin: 0;
    font-family: "Arimo", Arial, sans-serif;
    font-weight: 700;
    font-size: 33px;
    line-height: 60px;
    color: var(--white);
    text-align: right;
    width: 318px;
  }
  .contact span { display: block; }
</style>
</head>
<body>
  <section class="card card-front">
    <svg class="front-band" viewBox="0 0 1058 584" preserveAspectRatio="none" aria-hidden="true">
      <path d="M0,412 C90,452 200,488 420,418 C620,352 800,276 1058,268 L1058,584 L0,584 Z" fill="var(--red)"/>
    </svg>
    <h1 class="holder-name">Gareth Pollard</h1>
    <div class="name-rule"></div>
    <p class="holder-role">Unified Communications<br>and Network Architect</p>
    <div class="brand-mark">
      <span class="brand-dot"></span>
      <span class="brand-word">Halvex</span>
    </div>
    <p class="company-name">Halvex Consulting</p>
  </section>

  <section class="card card-back">
    <div class="back-mark">Halvex</div>
    <p class="contact">
      <span>www.halvex.com</span>
      <span>New Zealand</span>
    </p>
  </section>
</body>
</html>
```